Email Marketing Campaign Brief

We want to do an email marketing campaign around our consulting services. The attached documents provide back ground on our work but additional copy can be found below:

KV7pr is committed to helping you, the educator, make informed buying decisions based on local control and independent reviews through a simple, impartial and an effective approach.
In education, there exists a vast array of educational solutions – such as reading, science, language arts, and math curricula; school-wide reform programs; interventions; after-school programs; and new educational technologies. In the marketplace, providers could, and most do, claim to be able to improve educational outcomes and, in many cases, they all pretend to be supported by evidence. But a cursory review reveals that most evidence consists of poorly designed or advocacy-driven studies with some providers having such inadequate research as could only be described as case studies.

So the problem for State and local education officials is that they must sort through a myriad of such claims to decide which solutions merit consideration for their schools and classrooms. One US official stated the problem saying “many of these practitioners have seen interventions (solutions), introduced with great fanfare as being able to produce dramatic gains, come and go over the years, yielding little in the way of positive and lasting change – a perception confirmed by the flat achievement results over the past 30 years in the Federal Review of Scholastic Advancement long-term trend”

KV7pr is a process by which we make you, the educator, the locus of control

OUR Approach:
With four simple, yet highly effective steps, KV7pr guides educators through an informed buying process that’s based on local control and review.

Step 1 — Research, Review, and Evaluation Criteria

Step 2 — Cost / Benefit Analysis

Step 3 — Education Survey & Culture Scan

Step 4 — Negotiation & Representation

Target Market(s)

Education

Industry/Entity Type

Marketing

Font styles to use
Sans Serif

Colors
f9b46a
f37122

Requirements
Must have
• HTML format that can be used in an Email Campaign
Nice to have
• Additional Copy in Word

```html
<!DOCTYPE html>
<html lang="en">
<head>
<meta charset="utf-8">
<title>KV7pr — Research + Policy + Practice</title>
<link href="https://fonts.googleapis.com/css2?family=Montserrat:wght@400;600;700;800&family=Open+Sans:wght@400;600&display=swap" rel="stylesheet">
<style>
:root{
  --orange:#f37122;
  --peach:#f9b46a;
  --yellow:#f7c21a;
  --ink:#2d2d2d;
  --text:#8a8a8a;
  --line:#e7e7e7;
  --soft:#f2f2f2;
  --dark:#2b2b2b;
  --white:#ffffff;
}
*{margin:0;padding:0;box-sizing:border-box}
html,body{width:1200px;height:3464px;overflow:hidden;background:var(--white)}
body{font-family:"Open Sans",Arial,sans-serif;color:var(--text);position:relative}

/* header */
.site-header{height:112px;display:flex;align-items:center;justify-content:space-between;padding:0 140px 0 150px}
.brand{display:flex;align-items:center;gap:14px;font-family:"Montserrat",Arial,sans-serif;font-weight:700;font-size:34px;color:var(--ink)}
.brand-mark{width:30px;height:30px;background:var(--orange)}
.main-nav{display:flex;gap:36px;font-family:"Montserrat",Arial,sans-serif;font-weight:700;font-size:19px;letter-spacing:1px;color:var(--ink)}
.main-nav .active{color:var(--orange)}

/* hero */
.hero{position:relative;height:560px;text-align:center;color:var(--white)}
.hero-photo{position:absolute;inset:0;background:linear-gradient(135deg,#f6a064 0%,#f07a33 45%,#e0601a 100%)}
.hero-content{position:relative;padding-top:190px}
.hero-title{font-family:"Montserrat",Arial,sans-serif;font-weight:800;font-size:46px;letter-spacing:1px}
.hero-sub{margin-top:14px;font-family:"Montserrat",Arial,sans-serif;font-weight:600;font-size:24px;color:var(--yellow);letter-spacing:1px}
.btn-explore{display:inline-block;margin-top:64px;background:var(--yellow);color:var(--ink);font-family:"Montserrat",Arial,sans-serif;font-weight:700;font-size:17px;padding:14px 40px;border-radius:30px}

/* services */
.services{height:488px;display:flex;justify-content:center;gap:90px;padding-top:72px;border-bottom:2px solid var(--line)}
.service{width:210px;text-align:center}
.service-icon{width:128px;height:128px;border-radius:50%;background:var(--soft);margin:0 auto;display:flex;align-items:center;justify-content:center}
.service-icon.featured{background:var(--orange)}
.service-title{margin-top:42px;font-family:"Montserrat",Arial,sans-serif;font-weight:600;font-size:25px;color:var(--ink)}
.service-title.featured{color:var(--orange)}
.service-text{margin-top:16px;font-size:17px;line-height:28px;color:#9a9a9a}

/* welcome */
.welcome{height:640px;text-align:center;padding-top:92px}
.welcome-title{font-family:"Montserrat",Arial,sans-serif;font-weight:700;font-size:46px;color:var(--ink);letter-spacing:1px}
.welcome-title span{color:var(--orange)}
.welcome-text{width:900px;margin:40px auto 0;font-size:18px;line-height:32px}
.partner-badges{display:flex;justify-content:center;gap:28px;margin-top:58px}
.partner-badge{width:86px;height:86px;border-radius:50%;background:#e4e4e4;border:3px solid #cfcfcf}
.partner-marks{display:flex;justify-content:center;gap:34px;margin-top:34px}
.partner-mark{height:24px;background:#bdbdbd;border-radius:3px}

/* video */
.video{position:relative;height:532px;text-align:center;color:var(--white)}
.video-photo{position:absolute;inset:0;background:radial-gradient(ellipse at 40% 50%,#4a4a4a 0%,#333 55%,#242424 100%)}
.video-content{position:relative;padding-top:210px}
.video-title{font-family:"Montserrat",Arial,sans-serif;font-weight:600;font-size:38px;letter-spacing:2px}
.video-title span{color:var(--orange);font-weight:700}
.play-btn{width:66px;height:66px;border-radius:50%;background:var(--orange);margin:32px auto 0;display:flex;align-items:center;justify-content:center}

/* course */
.course{position:relative;height:840px}
.course-info{position:absolute;left:150px;top:60px;width:380px}
.course-title{font-family:"Montserrat",Arial,sans-serif;font-weight:700;font-size:40px;color:var(--ink);white-space:nowrap}
.course-sub{font-family:"Montserrat",Arial,sans-serif;font-size:14px;letter-spacing:2px;color:#a5a5a5;margin-top:4px}
.course-text{margin-top:34px;font-size:18px;line-height:32px}
.btn-learn{display:inline-block;margin-top:44px;background:var(--orange);color:var(--white);font-family:"Montserrat",Arial,sans-serif;font-weight:700;font-size:17px;padding:16px 36px;border-radius:30px}
.steps-graphic{position:absolute;left:550px;top:70px;width:520px;height:440px;background:linear-gradient(180deg,#f6f6f6 0%,#ececec 45%,#f7c9a3 100%)}

.testimonial{position:absolute;left:150px;top:490px;width:900px;height:300px;background:var(--white);box-shadow:0 6px 30px rgba(0,0,0,.12);text-align:center;padding-top:52px}
.testimonial-label{font-family:"Montserrat",Arial,sans-serif;font-weight:700;font-size:19px;color:var(--ink);letter-spacing:1px}
.testimonial-name{margin-top:22px;font-family:"Montserrat",Arial,sans-serif;font-weight:800;font-size:40px;color:var(--peach);letter-spacing:2px}
.testimonial-name .quote{color:var(--orange);margin-right:14px}
.testimonial-text{width:720px;margin:20px auto 0;font-size:17px;line-height:30px}

/* footer */
.site-footer{position:absolute;left:0;top:3188px;width:1200px;height:276px;background:var(--dark);color:var(--white);text-align:center;padding-top:92px}
.social-links{display:flex;justify-content:center;gap:44px;font-family:"Montserrat",Arial,sans-serif;font-weight:600;font-size:17px;letter-spacing:1px}
.social-links li{list-style:none;display:flex;align-items:center;gap:10px}
.social-dot{width:12px;height:12px;border-radius:50%;background:var(--white)}
.copyright{margin-top:30px;font-family:"Montserrat",Arial,sans-serif;font-weight:600;font-size:17px}
</style>
</head>
<body>

<header class="site-header">
  <div class="brand"><span class="brand-mark"></span>KV7pr</div>
  <nav class="main-nav"><span>RESEARCH</span><span class="active">POLICY</span><span>PRACTICE</span></nav>
</header>

<section class="hero">
  <div class="hero-photo" role="img" aria-label="Desk with alarm clock, books and pencils under an orange overlay"></div>
  <div class="hero-content">
    <h1 class="hero-title">RESEARCH + POLICY + PRACTICE</h1>
    <p class="hero-sub">ACTIONABLE RESEARCH IN EDUCATION</p>
    <span class="btn-explore">EXPLORE IT!</span>
  </div>
</section>

<section class="services">
  <div class="service">
    <div class="service-icon">
      <svg width="56" height="56" viewBox="0 0 56 56" fill="none" stroke="#f37122" stroke-width="3"><circle cx="10" cy="14" r="6"/><circle cx="46" cy="14" r="6"/><circle cx="28" cy="44" r="6"/><path d="M16 14h24M13 19l12 20M43 19L31 39"/></svg>
    </div>
    <h3 class="service-title">RESEARCH</h3>
    <p class="service-text">Our agency working on email template Design unique ideas</p>
  </div>
  <div class="service">
    <div class="service-icon featured">
      <svg width="56" height="56" viewBox="0 0 56 56" fill="none" stroke="#fff" stroke-width="3"><rect x="6" y="10" width="44" height="30" rx="2"/><path d="M22 48h12M28 40v8"/></svg>
    </div>
    <h3 class="service-title featured">POLICY</h3>
    <p class="service-text">Our agency working on email template Design unique ideas</p>
  </div>
  <div class="service">
    <div class="service-icon">
      <svg width="56" height="56" viewBox="0 0 56 56" fill="none" stroke="#f37122" stroke-width="3" stroke-linejoin="round"><path d="M28 6l10 14h-6v24h-8V20h-6z"/><path d="M20 50h16"/></svg>
    </div>
    <h3 class="service-title">PRACTICE</h3>
    <p class="service-text">Our agency working on email template Design unique ideas</p>
  </div>
</section>

<section class="welcome">
  <h2 class="welcome-title">WELCOME TO <span>KV7PR</span></h2>
  <p class="welcome-text">KV7pr partners with state and local entities to provide research, policy and practice deliverables that yield high value and actionable results. We offer a unique perspective on gathering data and understanding the policy effect and implications for developing models that yield mission critical change in a community, district or organization.</p>
  <div class="partner-badges">
    <span class="partner-badge"></span><span class="partner-badge"></span><span class="partner-badge"></span><span class="partner-badge"></span>
  </div>
  <div class="partner-marks">
    <span class="partner-mark" style="width:110px"></span>
    <span class="partner-mark" style="width:96px"></span>
    <span class="partner-mark" style="width:84px"></span>
    <span class="partner-mark" style="width:88px"></span>
    <span class="partner-mark" style="width:110px"></span>
  </div>
</section>

<section class="video">
  <div class="video-photo" role="img" aria-label="Hand sketching a diagram on a dark board"></div>
  <div class="video-content">
    <h2 class="video-title">WATCHING OUR <span>WORKING VIDEO</span></h2>
    <div class="play-btn"><svg width="22" height="24" viewBox="0 0 22 24"><path d="M4 2l16 10L4 22z" fill="#fff"/></svg></div>
  </div>
</section>

<section class="course">
  <div class="course-info">
    <h2 class="course-title">OUR COURSE</h2>
    <p class="course-sub">BECAUSE SKILLS PAY BILLS</p>
    <p class="course-text">Lorem ipsum dolor sit amet, consectetur adipiscing elit. Mauris blandit odio at sodales aliquet</p>
    <span class="btn-learn">LEARN MORE</span>
  </div>

  <div class="steps-graphic" role="img" aria-label="Staircase illustration of four steps toward local control and smart buying decisions, topped by an upward arrow"></div>

  <div class="testimonial">
    <p class="testimonial-label">OUR HAPPY CUSTOMERS</p>
    <p class="testimonial-name"><span class="quote">&ldquo;</span>LEO MARSH</p>
    <p class="testimonial-text">" Sed ut perspiciatis unde omnis iste natus error sit tatem accuantium dolorem-que laudantium, have a great features most tem totam.</p>
  </div>
</section>

<footer class="site-footer">
  <ul class="social-links">
    <li><span class="social-dot"></span>CIRCLEFEED</li>
    <li><span class="social-dot"></span>CHIRPLINE</li>
    <li><span class="social-dot"></span>SNAPGRID</li>
    <li><span class="social-dot"></span>SHOTBOARD</li>
  </ul>
  <p class="copyright">© 2017 All Right Reserved | KV7pr, LLC</p>
</footer>

</body>
</html>
```